Large corporation needs landing page for its employees with emotional and psychological problems

Vision:
Hello, we are a startup and would like to build a landing page and website in the mental health sector for a large corporation. In this site employees with emotional and psychological problems should quickly receive professional psychological support. This support takes the form of internal referrals from employees who are looking for help to qualified therapists, so that help can be provided quickly.
Furthermore, the employees get access to a tool where they can find out about topics in the mind health area and can also get help via webinars and podcasts. The employee should thus be able to take the hurdle to seek help and support in good time.
Therapists for whom the focus is on the urgency of providing quick help and support will work here in cooperation with the respective corporations.
Keywords:
• Help/Support
• overcome inhibitions
• Competent help
• Uncomplicated help
• Permanent access
• protected space
• Recognizing and naming emotional problems and actively tackling them
• get help
• mindfulness
• everyday helper
• Informative
• Anonymous
• compassion
• tolerance
• respect
• Appreciation
• empathy
• mindfulness
• protected space
• To be needed
• Like a lighthouse signal
What we need:
Landingpage
We need a landing page aimed at getting employees to contact psychological help. The call to action is to get in contact via a contact form.
Landing page content
There are several text modules:
• A heading/greeting
• A body of text at the beginning that explains the purpose of the page
• A bulleted text area describing the pain points and the solutions to them
Video:
The heart of the content will be a video explaining the need and inviting them to get in touch.
contact form:
It should be kept simple: first name, last name and email address
Legally required content:
General terms and conditions, data protection and imprint. These are only given as links in the footer.
In parallel, the Corporate Design should be adapted/extended:
Logo:
The font in the logo should be revised. The wings in the background remain.
Please adapt the logo for different uses:
• on a black background
• with transparent background
• favorite icon (browser)
• In square format for social media
Colors:
• develop a color chart based on the colors of the logo.
• please determine 2-3 main colors and the matching variations. I.e. transparent variations or light colors.
Typography:
Determine a decorative font and/or typography for headings and a text font. There should be no more than 3 fonts.
Updates
Need extra days to review
Industry/Entity Type
to recruit therapists as employees
Should not have
- please not to playful design or typography - and max. 3 colors

```html
<!DOCTYPE html>
<html lang="en">
<head>
<meta charset="UTF-8">
<title>Calm Harbor – Support for Employees</title>
<link href="https://fonts.googleapis.com/css2?family=Montserrat:wght@400;500;600;700;800&display=swap" rel="stylesheet">
<style>
:root{
  --teal:#0b5563;
  --teal-deep:#0a4450;
  --teal-soft:#3f7f84;
  --ink:#111111;
  --text:#333333;
  --muted:#9a9a9a;
  --paper:#f5f5f5;
  --white:#ffffff;
}
*{margin:0;padding:0;box-sizing:border-box}
html,body{width:1200px;height:5333px;overflow:hidden;background:var(--white)}
body{font-family:"Montserrat",sans-serif;color:var(--text);position:relative}
.page{position:relative;width:1200px;height:5333px;overflow:hidden}
.abs{position:absolute}
.btn{position:absolute;background:var(--teal);color:var(--white);font-weight:700;font-size:15px;display:flex;align-items:center;justify-content:center;border-radius:6px;text-decoration:none}
.btn--pill{border-radius:28px;font-size:16px}
h2{font-weight:700;color:var(--ink);font-size:35px;letter-spacing:.3px}
p{font-size:14.5px;line-height:26px}

/* header */
.site-header{top:0;left:0;width:1200px;height:84px;background:var(--white);z-index:5}
.brand{position:absolute;left:108px;top:18px;font-size:38px;font-weight:600;color:var(--teal);letter-spacing:-.5px}
.nav a{position:absolute;top:32px;font-size:13px;color:var(--ink);text-decoration:none}
.header-phone{position:absolute;left:935px;top:22px;display:flex;align-items:center;gap:8px;font-size:13px;font-weight:700;color:var(--ink)}
.header-phone .dot{width:32px;height:32px;border-radius:50%;background:var(--teal);display:flex;align-items:center;justify-content:center}

/* hero */
.hero-photo{top:84px;left:0;width:1200px;height:760px;background:linear-gradient(100deg,#1e1d1c 0%,#3a342f 40%,#6b4a33 70%,#8a6a55 100%)}
.hero-title{left:110px;top:243px;font-size:54px;font-weight:800;color:var(--white);line-height:64px;letter-spacing:1px}
.hero-text{left:110px;top:382px;width:450px;color:var(--white);font-size:15px;line-height:26px}
.hero-btn{left:110px;top:454px;width:168px;height:52px;font-size:13px}
.wave{left:0;width:1200px}

/* about */
.about-photo{left:116px;top:876px;width:450px;height:450px;border-radius:50%;background:radial-gradient(circle at 55% 45%,#caa08c 0%,#d8c4bd 35%,#ece8e6 70%)}
.about h2{left:595px;top:893px}
.about p{left:600px;top:950px;width:495px;font-size:13.5px;line-height:30px}
.about .btn{left:595px;top:1243px;width:159px;height:55px}

/* podcast */
.podcast-bg{left:0;top:1425px;width:1200px;height:590px;background:var(--paper)}
.podcast h2{left:0;top:1495px;width:1200px;text-align:center}
.podcast p.lead{left:220px;top:1553px;width:760px;text-align:center;font-size:14px}
.pod-card{position:absolute;width:297px;height:355px}
.pod-card .label{position:absolute;left:18px;bottom:30px;color:var(--white);font-weight:700;font-size:17px}
.player{position:absolute;width:274px;height:50px;background:var(--teal-deep);display:flex;align-items:center;padding:0 18px;gap:18px;color:var(--white);font-size:10px}
.player .track{flex:1;height:3px;background:#8fb3ba;position:relative;margin-top:8px}
.player .track::before{content:"";position:absolute;left:0;top:-5px;width:12px;height:12px;border-radius:50%;background:var(--white);border:2px solid var(--teal)}
.player .time{position:absolute;right:70px;top:8px}

/* therapists */
.ther-bg{left:0;top:2276px;width:1200px;height:741px;background:linear-gradient(100deg,#08505e 0%,#0b5563 55%,#2f7378 100%)}
.ther h2{left:110px;top:2363px;color:var(--white)}
.ther p{left:112px;width:505px;color:var(--white);font-size:13.5px}
.ther .link{left:143px;top:2773px;color:var(--white);font-weight:700;font-size:15px}
.ther-photo{left:631px;top:2352px;width:468px;height:468px;border-radius:50%;background:radial-gradient(circle at 50% 40%,#b07a5c 0%,#4b3b4a 45%,#1d2b45 75%)}

/* video carousel */
.slide-side{top:2948px;width:104px;height:407px;border:5px solid var(--white);box-shadow:0 3px 12px rgba(0,0,0,.15)}
.video-main{left:216px;top:2898px;width:769px;height:490px;background:linear-gradient(110deg,#d9cfc3 0%,#bfae9f 35%,#8a8078 55%,#e8e6e3 80%)}
.play{left:587px;top:3130px;width:56px;height:56px;border-radius:50%;background:var(--teal-deep);display:flex;align-items:center;justify-content:center}
.arrow{width:22px;height:22px;border-radius:50%;background:var(--teal);display:flex;align-items:center;justify-content:center}

/* webinar */
.webinar h2{left:0;top:3433px;width:1200px;text-align:center}
.webinar p{left:290px;top:3488px;width:620px;text-align:center;font-size:14px}
.webinar .btn{left:518px;top:3593px;width:165px;height:52px}

/* support */
.support-card{left:102px;top:3747px;width:991px;height:433px;background:var(--white);box-shadow:0 2px 20px rgba(0,0,0,.1)}
.support h2{left:175px;top:3826px}
.support p{left:176px;top:3888px;width:460px;font-size:13.5px}
.support .btn{left:176px;top:4003px;width:146px;height:52px}
.support-photo{left:707px;top:3772px;width:360px;height:380px;background:linear-gradient(135deg,#3a3330 0%,#5c4b40 40%,#2c2a30 75%,#4a4a52 100%)}

/* contact */
.contact-bg{left:0;top:4268px;width:1200px;height:700px;background:var(--paper)}
.contact h2{left:0;top:4328px;width:1200px;text-align:center}
.info{position:absolute;left:122px;display:flex;gap:18px}
.info .ico{width:52px;height:52px;border-radius:50%;border:2px solid var(--teal);display:flex;align-items:center;justify-content:center;flex-shrink:0}
.info h3{font-size:18px;font-weight:700;color:var(--ink);margin-top:2px}
.info span{display:block;font-size:14px;line-height:24px;width:200px}
.field{position:absolute;left:445px;width:317px;height:50px;background:var(--white);border:1px solid #e4e4e4;font-size:13px;color:var(--muted);padding:17px 22px}
.field--msg{left:783px;top:4405px;width:300px;height:255px}
.submit{left:445px;top:4608px;width:317px;height:52px;border-radius:0;font-size:15px}

/* footer */
.footer-bg{left:0;top:4820px;width:1200px;height:513px;background:var(--ink)}
.footer-brand{left:0;top:5000px;width:1200px;text-align:center;font-size:58px;font-weight:600;color:var(--teal)}
.footer-links{left:0;top:5133px;width:1200px;display:flex;justify-content:center;gap:44px;font-size:14px;color:var(--white)}
.copyright{left:0;top:5186px;width:1200px;text-align:center;font-size:12px;color:var(--white)}
.copyright a{color:var(--teal-soft)}
.social{left:499px;top:5229px;display:flex;gap:10px}
.social span{width:42px;height:42px;border-radius:50%;background:var(--teal)}
</style>
</head>
<body>
<div class="page">

  <!-- Header -->
  <header class="abs site-header">
    <div class="brand">calm harbor</div>
    <nav class="nav">
      <a style="left:430px">Home</a>
      <a style="left:508px">About Us</a>
      <a style="left:605px">Events</a>
      <a style="left:686px">Testimonial</a>
      <a style="left:802px">Contatc Us</a>
    </nav>
    <div class="header-phone">
      <span class="dot"><svg width="16" height="16" viewBox="0 0 24 24"><path fill="#fff" d="M6.6 10.8c1.4 2.8 3.8 5.1 6.6 6.6l2.2-2.2c.3-.3.7-.4 1-.2 1.1.4 2.3.6 3.6.6.6 0 1 .4 1 1V20c0 .6-.4 1-1 1C10.6 21 3 13.4 3 4c0-.6.4-1 1-1h3.5c.6 0 1 .4 1 1 0 1.3.2 2.5.6 3.6.1.3 0 .7-.2 1z"/></svg></span>
      +1 555 014 2270
    </div>
  </header>

  <!-- Hero -->
  <section class="hero">
    <div class="abs hero-photo" role="img" aria-label="Photo of a distressed woman covering her face with her hands"></div>
    <h1 class="abs hero-title">WELCOME TO<br>CALM HARBOR</h1>
    <p class="abs hero-text">Lorem ipsum dolor sit amet, consectetur adipiscing elit, sed do eiusmod tempor incididunt</p>
    <a class="btn hero-btn">GET STARTED</a>
    <svg class="abs wave" style="top:600px" width="1200" height="260" viewBox="0 0 1200 260">
      <path d="M0 95 C 250 40, 520 160, 700 190 C 880 215, 1060 160, 1200 70 L1200 260 L0 260 Z" fill="#fff"/>
    </svg>
  </section>

  <!-- About -->
  <section class="about">
    <div class="abs about-photo" role="img" aria-label="Photo of a worried young woman resting her chin on her hands"></div>
    <h2 class="abs">ABOUT CALM HARBOR</h2>
    <p class="abs">Lorem ipsum dolor sit amet, consectetur adipiscing elit, sed do eiusmod tempor incididunt ut labore et dolore magna aliqua. Quis ipsum suspendisse ultrices gravida. Risus commodo viverra maecenas accumsan lacus vel facilisis. Lorem ipsum dolor sit amet, consectetur adipiscing elit, sed do eiusmod tempor incididunt ut labore et dolore magna aliqua. Quis ipsum suspendisse ultrices gravida. Risus commodo viverra maecenas accumsan lacus vel facilisis. Lorem ipsum dolor sit amet, consectetur adipiscing elit, sed do eiusmod tempor incididunt ut labore et dolore magna aliqua.</p>
    <a class="btn">LEARN MORE</a>
  </section>

  <!-- Podcast -->
  <section class="podcast">
    <div class="abs podcast-bg"></div>
    <h2 class="abs">PODCAST</h2>
    <p class="abs lead">Lorem ipsum dolor sit amet, consectetur adipiscing elit, sed do eiusmod tempor incididunt ut labore et dolore magna aliqua. Quis ipsum suspendisse ultrices gravida. Risus commodo viverra maecenas accumsan lacus vel facilisis. Lorem ipsum dolor sit amet, consectetur adipiscing elit, sed do eiusmod tempor incididunt ut labore et dolore magna aliqua.</p>

    <div class="pod-card" style="left:109px;top:1695px;background:linear-gradient(180deg,#6b625a 0%,#3b3733 55%,#0d0d0d 100%)" role="img" aria-label="Photo of podcast microphones in a studio"><span class="label">Lorem Ipsum</span></div>
    <div class="player" style="left:120px;top:2040px">
      <svg width="14" height="14" viewBox="0 0 10 10"><path d="M8 1 L2 5 L8 9 Z" fill="#fff"/></svg>
      <svg width="14" height="14" viewBox="0 0 10 10"><circle cx="5" cy="5" r="4.5" fill="#fff"/><circle cx="5" cy="5" r="1.8" fill="#0a4450"/></svg>
      <svg width="14" height="14" viewBox="0 0 12 10"><path d="M1 3h2l3-2v8L3 7H1z" fill="#fff"/><path d="M8 3c1 1 1 3 0 4M10 2c1.6 1.6 1.6 4.4 0 6" stroke="#fff" fill="none"/></svg>
      <span class="time">0:00 / 4:16</span><span class="track"></span>
    </div>

    <div class="pod-card" style="left:449px;top:1772px;background:linear-gradient(180deg,#d6d4d2 0%,#7d7a78 55%,#101010 100%)" role="img" aria-label="Photo of a woman holding her hand to her chest"><span class="label">Lorem Ipsum</span></div>
    <div class="player" style="left:460px;top:2118px">
      <svg width="14" height="14" viewBox="0 0 10 10"><path d="M8 1 L2 5 L8 9 Z" fill="#fff"/></svg>
      <svg width="14" height="14" viewBox="0 0 10 10"><circle cx="5" cy="5" r="4.5" fill="#fff"/><circle cx="5" cy="5" r="1.8" fill="#0a4450"/></svg>
      <svg width="14" height="14" viewBox="0 0 12 10"><path d="M1 3h2l3-2v8L3 7H1z" fill="#fff"/><path d="M8 3c1 1 1 3 0 4M10 2c1.6 1.6 1.6 4.4 0 6" stroke="#fff" fill="none"/></svg>
      <span class="time">0:00 / 4:16</span><span class="track"></span>
    </div>

    <div class="pod-card" style="left:786px;top:1695px;background:linear-gradient(180deg,#8e8a86 0%,#4e4944 55%,#0d0d0d 100%)" role="img" aria-label="Photo of two people holding hands in comfort"><span class="label">Lorem Ipsum</span></div>
    <div class="player" style="left:797px;top:2040px">
      <svg width="14" height="14" viewBox="0 0 10 10"><path d="M8 1 L2 5 L8 9 Z" fill="#fff"/></svg>
      <svg width="14" height="14" viewBox="0 0 10 10"><circle cx="5" cy="5" r="4.5" fill="#fff"/><circle cx="5" cy="5" r="1.8" fill="#0a4450"/></svg>
      <svg width="14" height="14" viewBox="0 0 12 10"><path d="M1 3h2l3-2v8L3 7H1z" fill="#fff"/><path d="M8 3c1 1 1 3 0 4M10 2c1.6 1.6 1.6 4.4 0 6" stroke="#fff" fill="none"/></svg>
      <span class="time">0:00 / 4:16</span><span class="track"></span>
    </div>
  </section>

  <!-- Qualified therapists -->
  <section class="ther">
    <div class="abs ther-bg"></div>
    <h2 class="abs">QUALIFIED THERAPISTS</h2>
    <p class="abs" style="top:2425px">Lorem ipsum dolor sit amet, consectetur adipiscing elit, sed do eiusmod tempor incididunt ut labore et dolore magna aliqua. Quis ipsum suspendisse ultrices gravida. Risus commodo viverra maecenas accumsan lacus vel facilisis.</p>
    <p class="abs" style="top:2553px">Lorem ipsum dolor sit amet, consectetur adipiscing elit, sed do eiusmod tempor incididunt ut labore et dolore magna aliqua. Quis ipsum suspendisse ultrices gravida. Risus commodo viverra maecenas accumsan lacus vel facilisis.</p>
    <p class="abs" style="top:2682px">Lorem ipsum dolor sit amet, consectetur adipiscing elit, sed do eiusmod tempor incididunt ut labore</p>
    <a class="abs link">LEARN MORE</a>
    <div class="abs ther-photo" role="img" aria-label="Photo of a smiling therapist with arms crossed"></div>
  </section>

  <!-- Video carousel -->
  <section class="video">
    <div class="abs slide-side" style="left:112px;background:linear-gradient(180deg,#e7ddd0,#c8b8a6)" role="img" aria-label="Previous video thumbnail"></div>
    <div class="abs slide-side" style="left:984px;background:linear-gradient(180deg,#6f7d5a,#3a4630)" role="img" aria-label="Next video thumbnail"></div>
    <div class="abs video-main" role="img" aria-label="Video still of a physiotherapist treating a patient's leg"></div>
    <div class="abs play"><svg width="16" height="16" viewBox="0 0 10 10"><path d="M2 1 L9 5 L2 9 Z" fill="#fff"/></svg></div>
    <div class="abs arrow" style="left:102px;top:3149px"><svg width="10" height="10" viewBox="0 0 10 10"><path d="M7 1 L3 5 L7 9" stroke="#fff" stroke-width="2" fill="none"/></svg></div>
    <div class="abs arrow" style="left:1074px;top:3149px"><svg width="10" height="10" viewBox="0 0 10 10"><path d="M3 1 L7 5 L3 9" stroke="#fff" stroke-width="2" fill="none"/></svg></div>
  </section>

  <!-- Webinar -->
  <section class="webinar">
    <h2 class="abs">WEBINAR</h2>
    <p class="abs">Lorem ipsum dolor sit amet, consectetur adipiscing elit, sed do eiusmod tempor incididunt ut labore et dolore magna aliqua. Quis ipsum suspendisse ultrices gravida. Risus commodo viverra maecenas accumsan lacus vel facilisis.</p>
    <a class="btn btn--pill">Learn More</a>
  </section>

  <!-- Support -->
  <section class="support">
    <div class="abs support-card"></div>
    <h2 class="abs">SUPPORT</h2>
    <p class="abs">Lorem ipsum dolor sit amet, consectetur adipiscing elit, sed do eiusmod tempor incididunt ut labore et dolore magna aliqua. Quis ipsum suspendisse ultrices gravida. Risus commodo viverra maecenas accumsan lacus vel facilisis.</p>
    <a class="btn btn--pill">Learn More</a>
    <div class="abs support-photo" role="img" aria-label="Photo of two women in a supportive counselling conversation"></div>
  </section>

  <!-- Contact -->
  <section class="contact">
    <div class="abs contact-bg"></div>
    <h2 class="abs">CONTACT US</h2>
    <div class="info" style="top:4403px">
      <div class="ico"><svg width="20" height="20" viewBox="0 0 24 24"><path d="M12 2a7 7 0 0 0-7 7c0 5 7 13 7 13s7-8 7-13a7 7 0 0 0-7-7zm0 9.5A2.5 2.5 0 1 1 12 6.5a2.5 2.5 0 0 1 0 5z" fill="#0b5563"/></svg></div>
      <div><h3>Location</h3><span>199 b Calm Harbor Lorem ipsum dolor sit amet,</span></div>
    </div>
    <div class="info" style="top:4510px">
      <div class="ico"><svg width="20" height="20" viewBox="0 0 24 24"><path fill="#0b5563" d="M6.6 10.8c1.4 2.8 3.8 5.1 6.6 6.6l2.2-2.2c.3-.3.7-.4 1-.2 1.1.4 2.3.6 3.6.6.6 0 1 .4 1 1V20c0 .6-.4 1-1 1C10.6 21 3 13.4 3 4c0-.6.4-1 1-1h3.5c.6 0 1 .4 1 1 0 1.3.2 2.5.6 3.6.1.3 0 .7-.2 1z"/></svg></div>
      <div><h3>Phone</h3><span>+1 555 014 2270</span></div>
    </div>
    <div class="info" style="top:4605px">
      <div class="ico"><svg width="20" height="20" viewBox="0 0 24 24"><path d="M3 6h18v12H3z" fill="#0b5563"/><path d="M3 6l9 7 9-7" stroke="#fff" stroke-width="1.6" fill="none"/></svg></div>
      <div><h3>Email</h3><span>info@calmharbor.com</span></div>
    </div>
    <div class="field" style="top:4405px">First Name</div>
    <div class="field" style="top:4473px">Last Name</div>
    <div class="field" style="top:4540px">Email</div>
    <a class="btn submit">SUBMIT</a>
    <div class="field field--msg">Type your message</div>
  </section>

  <!-- Footer -->
  <footer>
    <div class="abs footer-bg"></div>
    <svg class="abs wave" style="top:4720px" width="1200" height="220" viewBox="0 0 1200 220">
      <path d="M0 0 H1200 V120 C 1050 60, 850 130, 650 150 C 430 170, 200 110, 0 150 Z" fill="#f5f5f5"/>
    </svg>
    <div class="abs footer-brand">calm harbor</div>
    <div class="abs footer-links"><span>General terms &amp; Conditions</span><span>Data Protection &amp; Imprint</span><span>About Us</span><span>Support</span></div>
    <div class="abs copyright">Copyright© 2023 <a>Calm Harbor</a> &nbsp;|&nbsp; All Rights Reserved</div>
    <div class="abs social" aria-label="Social media links"><span></span><span></span><span></span><span></span></div>
  </footer>

</div>
</body>
</html>
```